Building company buisness cards

We are looking for a sharp modern new look for our business cards.
We are a New Zealand based company that specialises in house and land packages.
We have attached a photo of the current logo and would like to see if it can be improved somehow if needed.
We are open to any colours but we have chosen green at this stage.
Feel free to change the font and make the logo smarter looking.
Play with the colours and see what looks best.

We want a card that looks so good know one will want to throw it away!

Target Market(s)

Home buyers

Industry/Entity Type

Building

Contact Information for Business Card

Dorian Keswick
0217392604
dkeswick@tidewellhomecraft.co.nz
tidewellhomecraft.co.nz

Font styles to use
Serif
Sans Serif

Colors

Designer to choose colors to be used in the design.

Requirements
Must have
• Logo and company name on one side, details on the other side
Nice to have
• Color codes for the original green are HEX #4a8028, RGB(74,128,40), CMYK(42,0,69,50)
• Round corners, Raised and/or spot UV

```html
<!DOCTYPE html>
<html lang="en">
<head>
<meta charset="utf-8">
<title>Tidewell Homecraft — Business Cards</title>
<link rel="stylesheet" href="https://fonts.googleapis.com/css2?family=Lato:wght@400;700;900&family=Oxygen:wght@400&display=swap">
<style>
  :root {
    --brand-green: #4a8028;
    --card-white: #f7f7f5;
    --text-grey: #6e6e6e;
    --rule-grey: #d6d6d6;
    --backdrop: #35302d;
  }
  * { margin: 0; padding: 0; box-sizing: border-box; }
  html, body {
    width: 1200px;
    height: 844px;
    overflow: hidden;
    background: var(--backdrop);
  }
  .canvas {
    position: relative;
    width: 1200px;
    height: 844px;
  }
  .card {
    position: absolute;
    top: 279px;
    width: 500px;
    height: 286px;
    border-radius: 6px;
    box-shadow: 0 10px 24px rgba(0,0,0,0.35);
    overflow: hidden;
  }
  .card--front {
    left: 70px;
    background: var(--card-white);
  }
  .card--back {
    left: 630px;
    background: var(--brand-green);
    display: flex;
    align-items: center;
    justify-content: center;
  }

  /* Front: company name block */
  .brand {
    position: absolute;
    top: 58px;
    left: 222px;
    width: 220px;
    text-align: center;
  }
  .brand__mark {
    display: block;
    width: 14px;
    height: 14px;
    margin: 0 auto 8px;
    border-radius: 50%;
    background: var(--brand-green);
  }
  .brand__name {
    font-family: "Lato", sans-serif;
    font-weight: 900;
    color: var(--brand-green);
    font-size: 30px;
    line-height: 0.95;
    letter-spacing: -0.5px;
  }
  .brand__rule {
    width: 90px;
    height: 1px;
    margin: 12px auto 0;
    background: var(--rule-grey);
  }

  /* Front: contact details */
  .contact {
    position: absolute;
    left: 34px;
    bottom: 30px;
  }
  .contact__name {
    font-family: "Lato", sans-serif;
    font-weight: 700;
    font-size: 17px;
    color: var(--brand-green);
    text-transform: uppercase;
    letter-spacing: 0.3px;
    margin-bottom: 14px;
  }
  .contact__list { list-style: none; }
  .contact__item {
    display: flex;
    align-items: center;
    gap: 7px;
    font-family: "Oxygen", sans-serif;
    font-size: 13px;
    color: var(--text-grey);
    line-height: 19px;
  }
  .contact__icon {
    width: 11px;
    height: 11px;
    flex: none;
    fill: var(--brand-green);
  }

  /* Back */
  .back-brand {
    font-family: "Lato", sans-serif;
    font-weight: 900;
    font-size: 36px;
    line-height: 1;
    color: #ffffff;
    text-align: center;
    letter-spacing: -0.5px;
  }
</style>
</head>
<body>
<main class="canvas">

  <section class="card card--front" aria-label="Business card front">
    <div class="brand">
      <span class="brand__mark" aria-hidden="true"></span>
      <div class="brand__name">tidewell<br>homecraft.</div>
      <div class="brand__rule"></div>
    </div>

    <div class="contact">
      <p class="contact__name">Dorian Keswick</p>
      <ul class="contact__list">
        <li class="contact__item">
          <svg class="contact__icon" viewBox="0 0 24 24" aria-hidden="true"><path d="M6.6 10.8a15.1 15.1 0 0 0 6.6 6.6l2.2-2.2c.3-.3.7-.4 1-.2 1.1.4 2.3.6 3.6.6.6 0 1 .4 1 1V20c0 .6-.4 1-1 1A17 17 0 0 1 3 4c0-.6.4-1 1-1h3.5c.6 0 1 .4 1 1 0 1.3.2 2.5.6 3.6.1.3 0 .7-.2 1z"/></svg>
          <span>0217392604</span>
        </li>
        <li class="contact__item">
          <svg class="contact__icon" viewBox="0 0 24 24" aria-hidden="true"><path d="M2 5h20v14H2z" fill="none"/><path d="M2 5h20v2l-10 6L2 7zm0 4l10 6 10-6v10H2z"/></svg>
          <span>dkeswick@tidewellhomecraft.co.nz</span>
        </li>
        <li class="contact__item">
          <svg class="contact__icon" viewBox="0 0 24 24" aria-hidden="true"><circle cx="12" cy="12" r="10"/><path d="M2 12h20M12 2c3 3 3 17 0 20M12 2c-3 3-3 17 0 20" stroke="#f7f7f5" stroke-width="1.5" fill="none"/></svg>
          <span>www.tidewellhomecraft.co.nz</span>
        </li>
      </ul>
    </div>
  </section>

  <section class="card card--back" aria-label="Business card back">
    <div class="back-brand">tidewell<br>homecraft.</div>
  </section>

</main>
</body>
</html>
```